Podcast Cover Art for Fast Growing Show (Ill include a gracious tip!)

This artwork is for "The Steadfast Fellow Show." The podcast is for men, and it's all about self-improvement, confidence, success, money, women and masculinity. It's for the guy who wants to improve himself. I'd like for my picture to be included — in black and white — and I want the text to read: "The Steadfast Fellow Show" and somewhere in there it'll say: "with Dale Prowen." I'm open to color schemes. The podcast is a little edgy so I'd like for that to be represented in the design. Thank you! (((Here's the podcast page if you wanna check it out: http://steadfastfellowshow.castorbit.net/)))

Target Market(s)

Men who want to attract women and improve their lives!

Font styles to use
Serif

Colors

Designer to choose colors to be used in the design.

Requirements
Must have
• My image in it (in black and white) and the two titles: "The Steadfast Fellow Show" and "with Dale Prowen"
Nice to have
• My logo in it somehow (which is the arrow looking logo attached below). I've also found that my image looks best in black and white and with a circular type cut out (although I'm open to different design ideas). I've attached my logo with a circular cut out below so you can see what I'm talking about.
Should not have
• Flowers. Teddy bears. ice cream.

```html
<!DOCTYPE html>
<html lang="en">
<head>
<meta charset="utf-8">
<title>The Steadfast Fellow Show — Cover Art</title>
<link rel="stylesheet" href="https://fonts.googleapis.com/css2?family=Barlow+Condensed:ital,wght@0,400;1,700&display=swap">
<style>
  :root {
    --bg-black: #050303;
    --bg-maroon: #3a0703;
    --frame-line: rgba(255,255,255,0.18);
    --ring-yellow: #ffd600;
    --dot-orange: #ffa61a;
    --portrait-white: #ffffff;
    --title-orange: #ffae17;
    --title-cream: #f3dcb1;
    --rule: rgba(255,255,255,0.75);
    --host-gold: #f0c64a;
  }
  html, body {
    margin: 0;
    width: 1200px;
    height: 1200px;
    overflow: hidden;
    background: var(--bg-black);
  }
  .cover {
    position: relative;
    width: 1200px;
    height: 1200px;
    overflow: hidden;
    background:
      radial-gradient(circle at 100% 100%, var(--bg-maroon) 0%, rgba(58,7,3,0.6) 30%, transparent 65%),
      radial-gradient(circle at 100% 0%, rgba(58,7,3,0.7) 0%, transparent 35%),
      linear-gradient(135deg, var(--bg-black) 40%, #1a0302 100%);
  }
  .cover__frame {
    position: absolute;
    inset: 14px;
    border: 1px solid var(--frame-line);
  }
  .cover__art {
    position: absolute;
    inset: 0;
  }
  .title {
    position: absolute;
    left: 0;
    top: 0;
    margin: 0;
    font-family: "Barlow Condensed", "Arial Narrow", sans-serif;
    font-weight: 700;
    font-style: italic;
    text-transform: uppercase;
    line-height: 1;
  }
  .title__line {
    position: absolute;
    white-space: nowrap;
    letter-spacing: 6px;
    background: linear-gradient(90deg, var(--title-orange) 0%, #ffc04a 45%, var(--title-cream) 100%);
    -webkit-background-clip: text;
    background-clip: text;
    color: transparent;
  }
  .title__line--the   { left: 228px; top: 800px; font-size: 104px; }
  .title__line--name  { left: 220px; top: 878px; font-size: 124px; letter-spacing: 8px; }
  .title__line--show  { left: 358px; top: 978px; font-size: 90px; }
  .host-rule {
    position: absolute;
    left: 324px;
    top: 1092px;
    width: 552px;
    height: 1px;
    background: var(--rule);
  }
  .host {
    position: absolute;
    left: 0;
    right: 0;
    top: 1120px;
    margin: 0;
    text-align: center;
    font-family: "Barlow Condensed", "Arial Narrow", sans-serif;
    font-weight: 400;
    font-size: 22px;
    letter-spacing: 3px;
    text-transform: uppercase;
    color: var(--host-gold);
  }
</style>
</head>
<body>
  <main class="cover">
    <div class="cover__frame"></div>

    <svg class="cover__art" width="1200" height="1200" viewBox="0 0 1200 1200" aria-hidden="false">
      <defs>
        <radialGradient id="halftoneGlow" cx="0.5" cy="0.5" r="0.5">
          <stop offset="0" stop-color="var(--dot-orange)" stop-opacity="0.55"/>
          <stop offset="1" stop-color="var(--dot-orange)" stop-opacity="0"/>
        </radialGradient>
        <linearGradient id="portraitTone" x1="0" y1="0" x2="0" y2="1">
          <stop offset="0" stop-color="#d8d8d8"/>
          <stop offset="0.35" stop-color="#8a8a8a"/>
          <stop offset="1" stop-color="#1a1a1a"/>
        </linearGradient>
        <clipPath id="portraitClip">
          <circle cx="588" cy="552" r="348"/>
        </clipPath>
      </defs>

      <!-- halftone arc area -->
      <path role="img" aria-label="Orange halftone dot arc"
            d="M 170 700 A 420 420 0 0 1 620 120 L 620 150 A 390 390 0 0 0 205 700 Z"
            fill="var(--dot-orange)" opacity="0.55"/>
      <ellipse role="img" aria-label="Orange halftone dot corner" cx="40" cy="1140" rx="150" ry="110" fill="url(#halftoneGlow)"/>
      <ellipse role="img" aria-label="Orange halftone dot corner" cx="1140" cy="60" rx="130" ry="110" fill="url(#halftoneGlow)"/>

      <!-- yellow ring -->
      <circle cx="604" cy="528" r="358" fill="var(--ring-yellow)"/>
      <!-- white portrait disc -->
      <circle cx="588" cy="552" r="348" fill="var(--portrait-white)"/>

      <!-- portrait placeholder -->
      <g clip-path="url(#portraitClip)">
        <path role="img" aria-label="Black and white portrait of the host, hands steepled in front of his chin"
              d="M 430 900 L 430 520 Q 430 260 600 250 Q 770 260 770 520 L 770 640 L 920 700 L 920 900 Z"
              fill="url(#portraitTone)"/>
      </g>
      <path role="img" aria-label="Host's steepled hands extending below the portrait circle"
            d="M 540 640 L 600 605 L 660 640 L 720 880 L 480 880 Z" fill="#9a9a9a" opacity="0.9"/>
    </svg>

    <h1 class="title">
      <span class="title__line title__line--the">The</span>
      <span class="title__line title__line--name">Steadfast</span>
      <span class="title__line title__line--show">Fellow Show</span>
    </h1>

    <div class="host-rule"></div>
    <p class="host">With Dale Prowen</p>
  </main>
</body>
</html>
```